NEW APP LAUNCH FOR HEALTHY CONCEPT RESTAURANT

We are looking for a design to post on our social media outlets, instagram and facebook to introduce our new app launch! We are looking for maybe a phone in the graphic, along with a catchy phrase or something along those lines. This app will manage customer accounts, and they can order take out, meal prep and delivery orders all through the app.

Target Market(s)

Ages 25-35 in Alberta Canada

```html
<!DOCTYPE html>
<html lang="en">
<head>
<meta charset="utf-8">
<title>Verdant App Launch – Social Posts</title>
<link rel="stylesheet" href="https://fonts.googleapis.com/css2?family=Montserrat:wght@300;500;700;800;900&family=Raleway:wght@200&display=swap">
<style>
  :root {
    --stage-light: #5b7c0c;
    --stage-dark: #3d5505;
    --lime: #95c11f;
    --lime-bright: #b8f200;
    --lime-glow: #b4dc3c;
    --ink: #000000;
    --paper: #ffffff;
    --phone-body: #2a2a2a;
    --phone-rim: #555555;
  }
  * { margin: 0; padding: 0; box-sizing: border-box; }
  html, body { width: 743px; height: 1200px; overflow: hidden; }
  body {
    position: relative;
    background: radial-gradient(ellipse at 50% 55%, var(--stage-light) 0%, var(--stage-dark) 85%);
    font-family: "Montserrat", sans-serif;
  }
  .post { position: absolute; display: block; box-shadow: 0 3px 6px rgba(0,0,0,.35); }
  .post--facebook { left: 93px; top: 103px; width: 557px; height: 557px; }
  .post--instagram { left: 90px; top: 779px; width: 564px; height: 296px; }
  .platform-label {
    position: absolute; left: 0; width: 743px; text-align: center;
    font-family: "Raleway", sans-serif; font-weight: 200;
    font-size: 35px; color: var(--paper); letter-spacing: 1px;
  }
  .platform-label--facebook { top: 670px; }
  .platform-label--instagram { top: 1086px; }
  .headline-heavy { font-family: "Montserrat", sans-serif; font-weight: 900; fill: var(--ink); stroke: var(--lime-bright); stroke-width: 5; paint-order: stroke; }
  .headline-mid { font-family: "Montserrat", sans-serif; font-weight: 700; fill: var(--ink); stroke: var(--lime-bright); stroke-width: 4; paint-order: stroke; }
  .slogan-light { font-family: "Montserrat", sans-serif; font-weight: 300; fill: var(--lime); }
  .slogan-dark { font-family: "Montserrat", sans-serif; font-weight: 500; fill: var(--ink); }
  .brand-name { font-family: "Montserrat", sans-serif; font-weight: 800; letter-spacing: 3px; }
</style>
</head>
<body>

<svg class="post post--facebook" viewBox="0 0 1133 1132" xmlns="http://www.w3.org/2000/svg">
  <defs>
    <radialGradient id="fb-glow" cx="0.5" cy="0.5" r="0.5">
      <stop offset="0" stop-color="#b4dc3c" stop-opacity="0.9"/>
      <stop offset="1" stop-color="#95c11f" stop-opacity="0"/>
    </radialGradient>
    <linearGradient id="photo-plate" x1="0" y1="0" x2="1" y2="1">
      <stop offset="0" stop-color="#f2f2f2"/><stop offset="1" stop-color="#c9a47a"/>
    </linearGradient>
    <linearGradient id="photo-burger" x1="0" y1="0" x2="1" y2="1">
      <stop offset="0" stop-color="#6a8a3a"/><stop offset="1" stop-color="#c98f4a"/>
    </linearGradient>
    <linearGradient id="photo-pizza" x1="0" y1="0" x2="1" y2="1">
      <stop offset="0" stop-color="#e9d9b8"/><stop offset="1" stop-color="#c9452e"/>
    </linearGradient>
    <radialGradient id="phone-shadow" cx="0.5" cy="0.5" r="0.5">
      <stop offset="0" stop-color="#000" stop-opacity="0.45"/><stop offset="1" stop-color="#000" stop-opacity="0"/>
    </radialGradient>
  </defs>

  <rect class="backdrop" width="1133" height="1132" fill="var(--lime)"/>
  <ellipse class="glow" cx="560" cy="790" rx="420" ry="380" fill="url(#fb-glow)"/>

  <path class="corner-black" d="M0 0 H182 L82 248 C140 330 165 410 142 490 C118 570 70 625 0 672 Z" fill="var(--ink)"/>
  <path class="corner-stripe" d="M182 0 H252 L140 234 C200 310 205 420 152 508 C180 420 168 330 108 250 Z" fill="var(--paper)"/>

  <path class="corner-black" d="M1133 520 C1045 590 990 680 1000 780 C1008 845 1035 880 1060 905 L965 1132 H1133 Z" fill="var(--ink)"/>
  <path class="corner-stripe" d="M998 672 C958 745 960 845 1012 905 L908 1132 H950 L1038 906 C996 862 975 770 998 672 Z" fill="var(--paper)"/>

  <path class="wave-white" d="M0 866 C80 870 125 850 172 790 C232 718 292 702 340 718 C378 732 398 748 412 760 L620 1078 L575 1132 H0 Z" fill="var(--paper)"/>

  <text class="headline-heavy" x="655" y="180" text-anchor="middle" font-size="142" textLength="805" lengthAdjust="spacingAndGlyphs">BEST FOOD</text>
  <text class="headline-mid" x="660" y="283" text-anchor="middle" font-size="102" textLength="405" lengthAdjust="spacingAndGlyphs">AT YOUR</text>
  <text class="headline-heavy" x="640" y="415" text-anchor="middle" font-size="142" textLength="775" lengthAdjust="spacingAndGlyphs">DOORSTEP</text>

  <g class="phone">
    <ellipse cx="550" cy="1088" rx="230" ry="12" fill="url(#phone-shadow)"/>
    <rect x="402" y="483" width="298" height="600" rx="42" fill="var(--phone-body)" stroke="var(--phone-rim)" stroke-width="6"/>
    <rect x="398" y="585" width="6" height="40" rx="3" fill="var(--phone-body)"/>
    <rect x="698" y="610" width="6" height="60" rx="3" fill="var(--phone-body)"/>
    <clipPath id="fb-screen"><rect x="420" y="502" width="262" height="562" rx="26"/></clipPath>
    <g clip-path="url(#fb-screen)">
      <rect x="420" y="502" width="262" height="210" fill="url(#photo-plate)" role="img" aria-label="Plated gourmet dish with fork and knife"/>
      <rect x="420" y="712" width="262" height="183" fill="url(#photo-burger)" role="img" aria-label="Burger with fresh basil and salad"/>
      <rect x="420" y="895" width="262" height="169" fill="url(#photo-pizza)" role="img" aria-label="Pizza with tomatoes and herbs"/>
    </g>
    <path d="M477 502 H625 V510 C625 520 618 526 608 526 H494 C484 526 477 520 477 510 Z" fill="var(--phone-body)"/>
  </g>

  <text class="slogan-light" x="372" y="942" text-anchor="end" font-size="54">EAT HEALTHY</text>
  <text class="slogan-light" x="372" y="997" text-anchor="end" font-size="54">LIVE LONG</text>

  <text class="brand-name" x="44" y="1080" font-size="52" fill="var(--ink)">VERDANT</text>
</svg>
<div class="platform-label platform-label--facebook">Facebook</div>

<svg class="post post--instagram" viewBox="0 0 1147 603" xmlns="http://www.w3.org/2000/svg">
  <defs>
    <radialGradient id="ig-glow" cx="0.5" cy="0.5" r="0.5">
      <stop offset="0" stop-color="#b4dc3c" stop-opacity="0.9"/>
      <stop offset="1" stop-color="#95c11f" stop-opacity="0"/>
    </radialGradient>
    <linearGradient id="ig-photo-plate" x1="0" y1="0" x2="1" y2="1">
      <stop offset="0" stop-color="#f2f2f2"/><stop offset="1" stop-color="#c9a47a"/>
    </linearGradient>
    <linearGradient id="ig-photo-burger" x1="0" y1="0" x2="1" y2="1">
      <stop offset="0" stop-color="#6a8a3a"/><stop offset="1" stop-color="#c98f4a"/>
    </linearGradient>
    <linearGradient id="ig-photo-pizza" x1="0" y1="0" x2="1" y2="1">
      <stop offset="0" stop-color="#e9d9b8"/><stop offset="1" stop-color="#c9452e"/>
    </linearGradient>
    <radialGradient id="ig-phone-shadow" cx="0.5" cy="0.5" r="0.5">
      <stop offset="0" stop-color="#000" stop-opacity="0.45"/><stop offset="1" stop-color="#000" stop-opacity="0"/>
    </radialGradient>
  </defs>

  <rect class="backdrop" width="1147" height="603" fill="var(--lime)"/>
  <ellipse class="glow" cx="270" cy="300" rx="300" ry="300" fill="url(#ig-glow)"/>

  <path class="corner-black" d="M0 0 H570 C515 65 455 100 400 115 L0 150 Z" fill="var(--ink)"/>
  <path class="corner-stripe" d="M0 170 L430 112 L405 132 L0 205 Z" fill="var(--paper)"/>

  <path class="wave-white" d="M0 470 C52 470 82 420 132 390 L330 603 H0 Z" fill="var(--paper)"/>

  <path class="corner-stripe" d="M695 472 C770 440 852 440 925 476 L1147 385 V412 L928 512 C858 472 772 462 695 472 Z" fill="var(--paper)"/>
  <path class="corner-black" d="M548 603 C602 530 690 474 790 474 C860 474 902 492 925 510 L1147 440 V603 Z" fill="var(--ink)"/>

  <g class="phone">
    <ellipse cx="272" cy="552" rx="180" ry="10" fill="url(#ig-phone-shadow)"/>
    <rect x="147" y="50" width="250" height="500" rx="36" fill="var(--phone-body)" stroke="var(--phone-rim)" stroke-width="5"/>
    <rect x="143" y="135" width="5" height="35" rx="2.5" fill="var(--phone-body)"/>
    <rect x="396" y="155" width="5" height="50" rx="2.5" fill="var(--phone-body)"/>
    <clipPath id="ig-screen"><rect x="162" y="66" width="220" height="468" rx="22"/></clipPath>
    <g clip-path="url(#ig-screen)">
      <rect x="162" y="66" width="220" height="175" fill="url(#ig-photo-plate)" role="img" aria-label="Plated gourmet dish with fork and knife"/>
      <rect x="162" y="241" width="220" height="152" fill="url(#ig-photo-burger)" role="img" aria-label="Burger with fresh basil and salad"/>
      <rect x="162" y="393" width="220" height="141" fill="url(#ig-photo-pizza)" role="img" aria-label="Pizza with tomatoes and herbs"/>
    </g>
    <path d="M210 66 H334 V72 C334 80 328 86 320 86 H224 C216 86 210 80 210 72 Z" fill="var(--phone-body)"/>
  </g>

  <text class="slogan-dark" x="505" y="147" font-size="48" textLength="567" lengthAdjust="spacingAndGlyphs">EAT HEALTHY, LIVE LONG</text>
  <text class="headline-heavy" x="505" y="243" font-size="112" textLength="590" lengthAdjust="spacingAndGlyphs">BEST FOOD</text>
  <text class="headline-mid" x="505" y="315" font-size="80" textLength="300" lengthAdjust="spacingAndGlyphs">AT YOUR</text>
  <text class="headline-heavy" x="505" y="415" font-size="112" textLength="565" lengthAdjust="spacingAndGlyphs">DOORSTEP</text>

  <text class="brand-name" x="1110" y="582" text-anchor="end" font-size="48" fill="var(--paper)">VERDANT</text>
</svg>
<div class="platform-label platform-label--instagram">Instagram</div>

</body>
</html>
```